Healthcare technology company needs website design

We need a logo for a new company based in the U.S. We develop software to assist consumers identifying lowest cost healthcare coverage methods, including insurance, discount cards, and cash options. We would like to see designs that use multiple shades of green with the optional addition of other complimentary colors. The final design should communicate a unique blend of saving money while receiving the healthcare you need.
Need the following pages/sections: Homepage, Solutions, About Us, Contact
Competitors: www.velorinhealth.example; www.qdplm.example

Target Market(s)

Businesses

Industry/Entity Type

Healthcare

Coding

Coded - Design and coding required

Number of Pages Required

4 page

Colors
0054AA
0677BA
7BADD7
CADEEF
E8F1F8
00AB8E
00BBA5
67D7C9
C6EFE9
E9F9F6

Requirements
Must have
• Matching color theme with logo
Nice to have
• Animated background

```html
<!DOCTYPE html>
<html lang="en">
<head>
<meta charset="utf-8">
<title>Fernleaf Health</title>
<link href="https://fonts.googleapis.com/css2?family=Montserrat:wght@500;600;700;800&family=Roboto:wght@400;500&display=swap" rel="stylesheet">
<style>
:root{
  --green:#2e8f43;
  --green-dark:#1f7a35;
  --teal:#168a7c;
  --blue:#1a7fcf;
  --blue-nav:#1e88d6;
  --ink:#1c1c1c;
  --text:#3d3d3d;
  --muted:#f3f4f5;
  --navy:#0c1b2f;
  --white:#ffffff;
}
*{box-sizing:border-box;margin:0;padding:0}
html,body{width:1200px;height:3963px;overflow:hidden}
body{position:relative;font-family:'Roboto',Arial,sans-serif;color:var(--text);background:var(--white)}
.abs{position:absolute}
h2.section-title{position:absolute;left:0;width:1200px;text-align:center;font-family:'Montserrat',sans-serif;font-weight:700;font-size:30px;color:var(--ink);letter-spacing:.3px}
.title-rule{position:absolute;height:3px;width:64px;background:var(--green)}
.btn{position:absolute;display:flex;align-items:center;justify-content:center;gap:9px;font-family:'Montserrat',sans-serif;font-weight:700;font-size:15px;color:var(--white);background:var(--teal);border-radius:3px}
.btn svg{width:14px;height:14px}

/* header */
.hero{left:0;top:0;width:1200px;height:728px;background:linear-gradient(135deg,#6f8596 0%,#aebfcb 35%,#8ea2b1 60%,#5d7486 100%)}
.hero-shade{left:0;top:0;width:1200px;height:728px;background:radial-gradient(ellipse at 50% 55%,rgba(20,40,60,.25),rgba(20,40,60,.05) 60%)}
.header-white{left:0;top:0;width:1200px;height:116px}
.brand{left:110px;top:30px;display:flex;align-items:center;gap:12px}
.brand-dot{width:52px;height:52px;border-radius:50%;background:var(--green)}
.brand-name{font-family:'Montserrat',sans-serif;font-weight:700;font-size:27px;color:var(--green);line-height:1.05}
.topbar{left:492px;top:22px;height:22px;display:flex;align-items:center;gap:9px;font-size:14px;color:#333;white-space:nowrap}
.topbar svg{width:16px;height:16px;flex:none}
.signup{left:965px;top:12px;width:123px;height:43px;font-size:14px}
.nav{left:476px;top:70px;height:46px;display:flex;align-items:center;font-family:'Roboto',sans-serif;font-size:16px;color:var(--white)}
.nav span.sep{margin:0 20px}
.hero-title{left:0;width:1200px;text-align:center;font-family:'Montserrat',sans-serif;font-weight:800;color:var(--white);text-shadow:0 2px 8px rgba(0,0,0,.35)}
.dots{left:566px;top:666px;display:flex;gap:8px}
.dots i{width:12px;height:12px;border-radius:50%;border:1.5px solid #fff;display:block}
.dots i.on{background:#fff}

/* feature cards */
.card{position:absolute;top:885px;width:242px;height:346px;color:var(--white);text-align:center}
.card.green{background:linear-gradient(160deg,#37a14b,#2a8a3f)}
.card.blue{background:linear-gradient(160deg,#2089dd,#1570c2)}
.card .ring{position:absolute;left:66px;top:32px;width:110px;height:110px;border-radius:50%;background:rgba(255,255,255,.25);display:flex;align-items:center;justify-content:center}
.card .ring span{width:90px;height:90px;border-radius:50%;background:#fff;display:flex;align-items:center;justify-content:center}
.card .ring svg{width:52px;height:52px}
.card h3{position:absolute;top:165px;width:100%;font-family:'Montserrat',sans-serif;font-weight:700;font-size:14px}
.card p{position:absolute;top:190px;left:14px;right:14px;font-size:14px;line-height:23px}
.card .outline{position:absolute;left:43px;top:275px;width:156px;height:45px;border:1.5px solid #fff;border-radius:3px;display:flex;align-items:center;justify-content:center;gap:10px;font-family:'Montserrat',sans-serif;font-weight:700;font-size:14px}

/* about */
.about-frame{left:0;top:1317px;width:614px;height:513px;border:1.5px solid var(--green);border-left:none}
.about-photo{left:0;top:1334px;width:597px;height:514px;background:linear-gradient(120deg,#b9c7d2,#e3e8ec 45%,#8ea1b0)}
.about-panel{left:614px;top:1334px;width:586px;height:494px;background:var(--muted)}
.about-title{left:684px;top:1400px;font-family:'Montserrat',sans-serif;font-weight:700;font-size:31px;color:var(--ink);line-height:38px}
.body-copy{font-size:15px;line-height:25.7px;color:var(--text)}

/* services */
.services-title{left:109px;top:1925px;font-family:'Montserrat',sans-serif;font-weight:700;font-size:31px;color:var(--ink)}
.slider-arrow{width:38px;height:38px;border-radius:50%;background:#fff;box-shadow:0 2px 8px rgba(0,0,0,.18);display:flex;align-items:center;justify-content:center}
.slider-arrow svg{width:14px;height:14px}
.dashboard{left:560px;top:1928px;width:560px;height:410px}

/* blog */
.blog{left:0;top:2425px;width:1200px;height:575px;background:linear-gradient(135deg,#2d8f41,#1f7d36)}
.post{position:absolute;top:2572px;height:358px;background:#fff;text-align:center}
.post .photo{position:absolute;left:0;top:0;width:100%;height:188px;background:linear-gradient(135deg,#4f6f86,#a6bccb 50%,#3a5a73)}
.post .date{position:absolute;top:173px;left:50%;transform:translateX(-50%);width:118px;height:35px;background:var(--green);color:#fff;font-family:'Montserrat',sans-serif;font-weight:700;font-size:14px;display:flex;align-items:center;justify-content:center}
.post h4{position:absolute;top:228px;width:100%;font-family:'Montserrat',sans-serif;font-weight:700;font-size:14px;color:var(--ink)}
.post p{position:absolute;top:252px;left:18px;right:18px;font-size:15px;line-height:26px;color:var(--text)}
.post a{position:absolute;top:318px;left:0;width:100%;font-size:15px;font-weight:500;color:var(--green);text-decoration:underline}

/* contact */
.contact-bg{left:0;top:3000px;width:1200px;height:585px;background:linear-gradient(180deg,#eef2f4,#f7f9fa)}
.field{position:absolute;height:43px;background:#fff;border:1px solid #d4d7da;display:flex;align-items:center;padding-left:24px;gap:12px;font-size:13px;color:#333}
.field svg{width:12px;height:12px}
.field.area{align-items:flex-start;padding-top:20px}

/* footer */
.footer{left:0;top:3585px;width:1200px;height:378px;background:var(--navy);color:#fff}
.foot-head{position:absolute;font-family:'Montserrat',sans-serif;font-weight:700;font-size:15px;text-decoration:underline}
.foot-list{position:absolute;list-style:none;font-size:15px}
.foot-list li{display:flex;align-items:center;gap:12px}
.foot-list li::before{content:"»";font-size:15px}
.contact-item{position:absolute;left:443px;display:flex;align-items:center;gap:16px;font-size:15px;line-height:20px}
.contact-item .ic{width:32px;height:32px;border:1.5px solid #fff;border-radius:50%;display:flex;align-items:center;justify-content:center;flex:none}
.contact-item svg{width:14px;height:14px}
.social{position:absolute;top:3829px;width:32px;height:32px;border-radius:50%}
</style>
</head>
<body>

<!-- hero -->
<div class="abs hero" role="img" aria-label="Photo of two scientists working in a laboratory"></div>
<div class="abs hero-shade"></div>

<svg class="abs header-white" viewBox="0 0 1200 116" aria-hidden="true">
  <polygon points="0,0 1200,0 1200,70 476,70 455,116 0,116" fill="#ffffff"/>
  <polygon points="455,116 476,70 1200,70 1200,116" fill="var(--blue-nav)"/>
</svg>

<div class="abs brand">
  <div class="brand-dot"></div>
  <div class="brand-name">FERNLEAF<br>HEALTH</div>
</div>

<div class="abs topbar">
  <svg viewBox="0 0 16 16"><rect width="16" height="16" rx="3" fill="#1e88d6"/><path d="M5 4l2 2-1 1c.6 1.3 1.7 2.4 3 3l1-1 2 2-1.3 1.3C7.5 12 4 8.5 3.7 5.3z" fill="#fff"/></svg>
  <span>|</span><span>Call:+1 555 010 0188</span>
  <svg viewBox="0 0 16 16" style="margin-left:10px"><rect y="3" width="16" height="11" rx="1" fill="#1e88d6"/><path d="M1 4l7 5 7-5" stroke="#fff" stroke-width="1.4" fill="none"/></svg>
  <span>|</span><span>Email: info@fernleaf.example</span>
</div>
<div class="btn signup">SIGN UP
  <svg viewBox="0 0 14 14"><circle cx="7" cy="4" r="3" fill="#fff"/><path d="M1.5 13c0-3.3 2.5-5 5.5-5s5.5 1.7 5.5 5z" fill="#fff"/></svg>
</div>
<nav class="abs nav">
  <span style="margin-left:14px">Home</span><span class="sep">|</span><span>About</span><span class="sep">|</span><span>Services</span><span class="sep">|</span><span>Why choose Us</span><span class="sep">|</span><span>Blog</span><span class="sep">|</span><span>Contact us</span>
</nav>

<div class="abs hero-title" style="top:376px;font-size:46px">WELCOME TO</div>
<div class="abs hero-title" style="top:444px;font-size:58px">FERNLEAF HEALTH</div>
<div class="btn" style="left:517px;top:550px;width:166px;height:51px">GET STARTED
  <svg viewBox="0 0 14 14"><circle cx="7" cy="7" r="6.5" fill="#fff"/><path d="M6 4l3 3-3 3" stroke="#168a7c" stroke-width="1.8" fill="none"/></svg>
</div>
<div class="abs dots"><i class="on"></i><i></i><i></i><i></i></div>

<!-- software development -->
<h2 class="section-title" style="top:806px">SOFTWARE DEVELOPMENT</h2>
<div class="title-rule" style="left:572px;top:845px"></div>

<div class="card green" style="left:101px">
  <div class="ring"><span><svg viewBox="0 0 52 52"><path d="M26 22c-6-5-11-9-11-13a5 5 0 0 1 11-1 5 5 0 0 1 11 1c0 4-5 8-11 13z" fill="#2e8f43"/><path d="M6 34l8-4h10l10 2 10-6 3 3-13 10-14 2-14-3z" fill="#1a7fcf"/></svg></span></div>
  <h3>COVERAGE METHODS</h3>
  <p>Lorem ipsum dolor sit amet consectetur adipiscing elit sed eiusmod tempor incididunt.</p>
  <div class="outline">LEARN MORE <svg width="16" height="10" viewBox="0 0 16 10"><path d="M0 5h14M10 1l4 4-4 4" stroke="#fff" stroke-width="1.8" fill="none"/></svg></div>
</div>
<div class="card blue" style="left:353px">
  <div class="ring"><span><svg viewBox="0 0 52 52"><circle cx="26" cy="14" r="6" fill="#2e8f43"/><circle cx="15" cy="28" r="5" fill="#1a7fcf"/><circle cx="37" cy="28" r="5" fill="#1a7fcf"/><path d="M6 46c0-7 4-11 9-11s9 4 9 11zM28 46c0-7 4-11 9-11s9 4 9 11z" fill="#1a7fcf"/></svg></span></div>
  <h3>INCLUDING INSURANCE</h3>
  <p>Lorem ipsum dolor sit amet consectetur adipiscing elit sed eiusmod tempor incididunt.</p>
  <div class="outline">LEARN MORE <svg width="16" height="10" viewBox="0 0 16 10"><path d="M0 5h14M10 1l4 4-4 4" stroke="#fff" stroke-width="1.8" fill="none"/></svg></div>
</div>
<div class="card green" style="left:605px">
  <div class="ring"><span><svg viewBox="0 0 52 52"><rect x="20" y="16" width="24" height="28" rx="3" fill="#1a7fcf"/><path d="M30 22h4v5h5v4h-5v5h-4v-5h-5v-4h5z" fill="#fff"/><path d="M6 20h6l3-6 4 12 3-6h4" stroke="#2e8f43" stroke-width="2.5" fill="none"/></svg></span></div>
  <h3>DISCOUNT CARDS</h3>
  <p>Lorem ipsum dolor sit amet consectetur adipiscing elit sed eiusmod tempor incididunt.</p>
  <div class="outline">LEARN MORE <svg width="16" height="10" viewBox="0 0 16 10"><path d="M0 5h14M10 1l4 4-4 4" stroke="#fff" stroke-width="1.8" fill="none"/></svg></div>
</div>
<div class="card blue" style="left:857px">
  <div class="ring"><span><svg viewBox="0 0 52 52"><circle cx="18" cy="12" r="5" fill="#2e8f43"/><circle cx="34" cy="12" r="5" fill="#1a7fcf"/><rect x="12" y="20" width="12" height="14" rx="2" fill="#2e8f43"/><rect x="28" y="20" width="12" height="14" rx="2" fill="#1a7fcf"/><rect x="14" y="34" width="3" height="10" fill="#2e8f43"/><rect x="19" y="34" width="3" height="10" fill="#2e8f43"/><rect x="30" y="34" width="3" height="10" fill="#1a7fcf"/><rect x="35" y="34" width="3" height="10" fill="#1a7fcf"/></svg></span></div>
  <h3>CASH OPTIONS</h3>
  <p>Lorem ipsum dolor sit amet consectetur adipiscing elit sed eiusmod tempor incididunt.</p>
  <div class="outline">LEARN MORE <svg width="16" height="10" viewBox="0 0 16 10"><path d="M0 5h14M10 1l4 4-4 4" stroke="#fff" stroke-width="1.8" fill="none"/></svg></div>
</div>

<!-- about -->
<div class="abs about-frame"></div>
<div class="abs about-panel"></div>
<div class="abs about-photo" role="img" aria-label="Photo of a researcher at a microscope and computer in a laboratory"></div>
<h2 class="abs about-title">ABOUT<br>FERNLEAF HEALTH</h2>
<div class="title-rule" style="left:684px;top:1484px"></div>
<p class="abs body-copy" style="left:684px;top:1502px;width:432px">Lorem ipsum dolor sit amet, consectetur adipiscing elit, sed do eiusmod tempor incididunt ut labore et dolore magna aliqua ad minim veniam, quis nostrud exercitation ullamco laboris nisi ut aliquip commodo consequat Duis aute irure reprehendervolup velit esse cillum dolore eu fugiat nulla pariatur. Excepteur sinte Lorem ipsum dolor sit amet, consectetur adipiscing elit sed do eiusmod tempor incididunt ut labore et dolore magna .</p>
<div class="btn" style="left:684px;top:1700px;width:167px;height:51px">LEARN MORE
  <svg viewBox="0 0 14 14"><circle cx="7" cy="7" r="6.5" fill="#fff"/><path d="M6 4l3 3-3 3" stroke="#168a7c" stroke-width="1.8" fill="none"/></svg>
</div>

<!-- services -->
<h2 class="abs services-title">OUR SERVICES</h2>
<div class="title-rule" style="left:109px;top:1963px"></div>
<p class="abs body-copy" style="left:109px;top:1986px;width:432px">Lorem ipsum dolor sit amet, consectetur adipiscing elit, sed do eiusmod tempor incididunt ut labore et dolore magna enim ad minim veniam, quis nostrud exercitation ullamco laboris nisi ut aliquip commodo consequat Duis aute irure reprehenderlop velit esse cillum dolore eu fugiat nulla pariatur. Excepteur sinte Lorem ipsum dolor sit amet, consectetur adipiscing elit sed do eiusmod tempor incididunt ut labore et dolore magna enim ad minim veniam quis nostrud exercitation laborisorem ipsum do consectetur adipiscing elit sed do eiusmod tempor.</p>
<div class="btn" style="left:109px;top:2238px;width:167px;height:51px">LEARN MORE
  <svg viewBox="0 0 14 14"><circle cx="7" cy="7" r="6.5" fill="#fff"/><path d="M6 4l3 3-3 3" stroke="#168a7c" stroke-width="1.8" fill="none"/></svg>
</div>
<div class="abs dashboard" role="img" aria-label="Illustration of a laptop showing an analytics dashboard in front of a blue circle">
  <svg width="560" height="410" viewBox="0 0 560 410">
    <circle cx="375" cy="204" r="205" fill="#1a7fcf"/>
    <rect x="80" y="44" width="410" height="290" rx="10" fill="#e3e9ef"/>
    <rect x="0" y="330" width="560" height="16" rx="6" fill="#c9d1d8"/>
  </svg>
</div>
<div class="abs slider-arrow" style="left:33px;top:2113px"><svg viewBox="0 0 14 14"><path d="M9 2L4 7l5 5" stroke="#222" stroke-width="2" fill="none"/></svg></div>
<div class="abs slider-arrow" style="left:1128px;top:2113px"><svg viewBox="0 0 14 14"><path d="M5 2l5 5-5 5" stroke="#222" stroke-width="2" fill="none"/></svg></div>

<!-- blog -->
<div class="abs blog"></div>
<h2 class="section-title" style="top:2487px;color:#fff">LATEST BLOG</h2>
<div class="title-rule" style="left:568px;top:2527px;background:#fff"></div>

<article class="post" style="left:111px;width:281px">
  <div class="photo" role="img" aria-label="Photo of two doctors reviewing a tablet"></div>
  <div class="date">May 13.5.2022</div>
  <h4>LOREM IPSUM DOLOR SIT AMET</h4>
  <p>Lorem ipsum dolor sit consectetur adipiscing elit sed do eiusmod</p>
  <a>Read More</a>
</article>
<article class="post" style="left:422px;width:356px">
  <div class="photo" role="img" aria-label="Photo of researchers working at lab computers"></div>
  <div class="date">May 13.5.2022</div>
  <h4>LOREM IPSUM DOLOR SITED AMETED</h4>
  <p>Lorem ipsum dolor sit consectetur adipiscing elit sed do eiusmod tempor incididunt ut</p>
  <a>Read More</a>
</article>
<article class="post" style="left:808px;width:283px">
  <div class="photo" role="img" aria-label="Photo of a scientist in protective gear with digital overlays"></div>
  <div class="date">May 13.5.2022</div>
  <h4>LOREM IPSUM DOLOR SIT AMET</h4>
  <p>Lorem ipsum dolor sit consectetur adipiscing elit sed do eiusmod</p>
  <a>Read More</a>
</article>

<!-- contact -->
<div class="abs contact-bg"></div>
<h2 class="section-title" style="top:3069px">GET IN TOUCH</h2>
<div class="title-rule" style="left:568px;top:3109px"></div>

<div class="field" style="left:160px;top:3152px;width:433px"><svg viewBox="0 0 12 12"><circle cx="6" cy="3.5" r="3" fill="#222"/><path d="M0 12c0-3 3-5 6-5s6 2 6 5z" fill="#222"/></svg>First Name</div>
<div class="field" style="left:607px;top:3152px;width:433px"><svg viewBox="0 0 12 12"><circle cx="6" cy="3.5" r="3" fill="#222"/><path d="M0 12c0-3 3-5 6-5s6 2 6 5z" fill="#222"/></svg>Last Name</div>
<div class="field" style="left:160px;top:3215px;width:433px"><svg viewBox="0 0 12 12"><rect y="2" width="12" height="9" fill="#222"/><path d="M0 3l6 4 6-4" stroke="#fff" fill="none"/></svg>Email</div>
<div class="field" style="left:607px;top:3215px;width:433px"><svg viewBox="0 0 12 12"><rect x="3" y="0" width="6" height="12" rx="1" fill="#222"/><rect x="4" y="1.5" width="4" height="8" fill="#fff"/></svg>Phone</div>
<div class="field area" style="left:160px;top:3277px;width:880px;height:146px"><svg viewBox="0 0 12 12"><ellipse cx="6" cy="5" rx="6" ry="4.2" fill="#222"/><path d="M2 8l-1 3 4-2z" fill="#222"/></svg>Comments</div>
<div class="btn" style="left:535px;top:3455px;width:130px;height:45px">SUBMIT
  <svg viewBox="0 0 14 14"><path d="M1 7l12-6-4 12-2-5z" fill="#fff"/></svg>
</div>

<!-- footer -->
<footer class="abs footer"></footer>
<div class="abs brand" style="top:3650px">
  <div class="brand-dot" style="width:44px;height:44px"></div>
  <div class="brand-name" style="font-size:22px">FERNLEAF<br>HEALTH</div>
</div>
<p class="abs" style="left:110px;top:3722px;font-size:15px;line-height:24px;color:#fff">Lorem ipsum dolor sited ameted<br>consectetur adipiscing elit sed</p>
<div class="foot-head" style="left:110px;top:3784px;color:#fff">FOLLOW ON</div>
<div class="social" style="left:110px;background:#2f4f9a"></div>
<div class="social" style="left:152px;background:#1da1f2"></div>
<div class="social" style="left:190px;background:#d63a3a"></div>
<div class="social" style="left:231px;background:#b8963e"></div>

<div class="foot-head" style="left:443px;top:3640px;color:#fff">CONTACT US</div>
<div class="contact-item" style="top:3694px;color:#fff"><span class="ic"><svg viewBox="0 0 14 14"><path d="M3 1l3 3-1.5 1.5c.8 1.7 2.3 3.2 4 4L10 8l3 3-2 2C6 12.5 1.5 8 1 3z" fill="#fff"/></svg></span>+1 555 010 0188</div>
<div class="contact-item" style="top:3752px;color:#fff"><span class="ic"><svg viewBox="0 0 14 14"><rect y="3" width="14" height="9" rx="1" fill="none" stroke="#fff" stroke-width="1.4"/><path d="M1 4l6 4 6-4" stroke="#fff" stroke-width="1.4" fill="none"/></svg></span>info@fernleaf.example</div>
<div class="contact-item" style="top:3810px;color:#fff"><span class="ic"><svg viewBox="0 0 14 14"><path d="M7 13s-5-5-5-8a5 5 0 0 1 10 0c0 3-5 8-5 8z" fill="#fff"/><circle cx="7" cy="5" r="1.8" fill="#0c1b2f"/></svg></span>117,Lorem ipsum dolor<br>consectetur adipiscing.</div>

<div class="foot-head" style="left:741px;top:3640px;color:#fff">OTHERLINKS</div>
<ul class="foot-list" style="left:741px;top:3680px;color:#fff;line-height:30px">
  <li>Team</li><li>FAQ</li><li>Services</li><li>Privacy</li><li>Policy</li>
</ul>
<div class="foot-head" style="left:963px;top:3640px;color:#fff">QUICKLINKS</div>
<ul class="foot-list" style="left:963px;top:3680px;color:#fff;line-height:37px">
  <li>Home</li><li>About</li><li>Services</li><li>Why choose Us</li><li>Contact us</li>
</ul>

<div class="abs" style="left:110px;top:3905px;width:980px;height:1px;background:rgba(255,255,255,.35)"></div>
<p class="abs" style="left:0;top:3927px;width:1200px;text-align:center;font-size:14px;color:#fff">© 2022 Copyrights&nbsp; Fernleaf&nbsp; All Rights Reserved.</p>

</body>
</html>
```